Corvimo Business Card

Corvimo is a young and energetic software development consultancy. We spend our time on the road working with clients on their sites an meeting new potential customers and employees!

We need a sharp, vibrant and memorable business card that will inspires those that receive it to look after it as it oozes quality and is a nice thing in its own right.

We like bold colours and distinctive design. So show us what you can do.

In terms of information on the card, it would be good to see:

* Our logo (Obviously :) )
* Employee name
* Email
* Website address
* Mobile number
* Full company name (Corvimo ltd)
* Registered company number
* Registered company address

Industry/Entity Type

Software

Requirements
Nice to have
• We are thinking that having a QR Code on the business card could be a good way of adding active marketing. It would be good to see if you are able to merge the kind of element in to your designs!

Maybe something special could be achieved using a visual QR Code like those produced at http://www.pixoranta.example/ ? You have our media so feel free to have a play.

```html
<!DOCTYPE html>
<html lang="en">
<head>
<meta charset="utf-8">
<title>Corvimo Business Card</title>
<link rel="stylesheet" href="https://fonts.googleapis.com/css2?family=Open+Sans:wght@400;600&display=swap">
<style>
  :root {
    --brand-red: #c01c2e;
    --brand-red-light: #ea7282;
    --card-white: #ffffff;
    --text-grey: #8a8a8a;
    --pattern-grey: #b3b3b3;
    --stage-light: #ffffff;
    --stage-edge: #e9e9e9;
  }
  * { margin: 0; padding: 0; box-sizing: border-box; }
  html, body { width: 1200px; height: 900px; overflow: hidden; }
  body { font-family: "Open Sans", Arial, sans-serif; background: var(--card-white); }
  .canvas { position: relative; width: 1200px; height: 900px; }
  .stage {
    position: absolute; left: 0; top: 0; width: 1200px; height: 695px;
    background: radial-gradient(ellipse 700px 420px at 600px 340px, var(--stage-light) 40%, var(--stage-edge) 100%);
  }
  .card {
    position: absolute; left: 401px; width: 401px; height: 230px;
    border-radius: 22px; overflow: hidden;
    box-shadow: 0 3px 10px rgba(0,0,0,0.14);
  }
  .card-front { top: 100px; background: var(--brand-red); }
  .card-back { top: 367px; background: var(--card-white); }
  .front-pattern {
    position: absolute; left: 0; top: 0; width: 200px; height: 230px;
    background: linear-gradient(90deg, var(--brand-red-light) 0%, #e04a5c 55%, var(--brand-red) 100%);
  }
  .back-pattern {
    position: absolute; right: 0; top: 0; width: 174px; height: 230px;
    background: linear-gradient(90deg, var(--card-white) 0%, #dedede 40%, var(--pattern-grey) 100%);
  }
  .wordmark { position: absolute; font-weight: 600; letter-spacing: 0.5px; line-height: 1; }
  .wordmark-front { left: 212px; top: 101px; font-size: 27px; color: var(--card-white); }
  .wordmark-footer { left: 828px; top: 776px; font-size: 42px; color: var(--brand-red); }
  .holder-name { position: absolute; left: 77px; top: 27px; font-size: 18px; color: var(--brand-red); line-height: 1; }
  .holder-role { position: absolute; left: 77px; top: 48px; font-size: 12px; color: var(--brand-red); line-height: 1; }
  .contact-list { position: absolute; left: 55px; top: 73px; list-style: none; }
  .contact-list li { display: flex; align-items: center; height: 17.5px; font-size: 11px; color: var(--text-grey); }
  .contact-list svg { width: 12px; height: 12px; margin-right: 11px; fill: var(--text-grey); }
  .company-details { position: absolute; left: 78px; top: 142px; font-size: 9px; line-height: 11.5px; color: var(--text-grey); }
</style>
</head>
<body>
<div class="canvas">
  <div class="stage"></div>

  <section class="card card-front">
    <div class="front-pattern" role="img" aria-label="Red pixel-square pattern fading into the card"></div>
    <div class="wordmark wordmark-front">CORVIMO</div>
  </section>

  <section class="card card-back">
    <div class="holder-name">ALEX MARLOW</div>
    <div class="holder-role">PRESIDENT</div>
    <ul class="contact-list">
      <li><svg viewBox="0 0 12 12"><path d="M1 3h10v7H1z M1 3l5 4 5-4" fill="var(--text-grey)"/><path d="M1.5 3.5l4.5 3.5 4.5-3.5" stroke="#fff" stroke-width="0.9" fill="none"/></svg>alex@corvimo.example</li>
      <li><svg viewBox="0 0 12 12"><circle cx="6" cy="6" r="5"/><path d="M1 6h10M6 1c-2.5 3-2.5 7 0 10M6 1c2.5 3 2.5 7 0 10" stroke="#fff" stroke-width="0.8" fill="none"/></svg>www.corvimo.example</li>
      <li><svg viewBox="0 0 12 12"><rect x="3" y="1" width="6" height="10" rx="1.2"/><rect x="4" y="2.5" width="4" height="4" fill="#fff"/></svg>(000) 000-0000</li>
    </ul>
    <p class="company-details">Corvimo ltd<br>Lorem ipsum dolor<br>sit amet,<br>consectetuer a<br>dipiscing elit,<br>sed diam</p>
    <div class="back-pattern" role="img" aria-label="Grey pixel-square pattern fading into the card"></div>
  </section>

  <div class="wordmark wordmark-footer">CORVIMO</div>
</div>
</body>
</html>
```